IT Services

We come to you
Only $49/hr
No contract, no monthly fee
Software engineer on staff
remote assistance or visit in your office

On the back of the card I want to list services.

- Server setup
- Network troubleshooting
- Printer setup
- Secure backup setup
- Software installation
- Wireless network setup
- Wired network setup
- Disaster recovery
- Website management
- Any other technology related support
- Email setup
- HIPAA compliance review and setup
Updates

the URL is: GEARFIXPRO.ZONE please use it on the card

On the card we need to mention "Connect remotely to address your IT issues" if there is enough room as well as "we go to you"

Industry/Entity Type

Printer

Contact Information for Business Card

I want a busoiness card to offer my services to doctor offices, it can be dentists, Otamatry, and other professions. I provide the following service. My plan is to go to their office and drop off my card. I don't want them to forget about it that is why I am paying for the design. I like hand writing design formats.

```html
<!DOCTYPE html>
<html lang="en">
<head>
<meta charset="utf-8">
<title>GearFix Pro – Business Card</title>
<link rel="stylesheet" href="https://fonts.googleapis.com/css2?family=Kalam:wght@400;700&family=Patrick+Hand&family=Open+Sans:wght@400;600&display=swap">
<style>
  :root {
    --backdrop: #e8e5e0;
    --card: #ffffff;
    --lavender: #a9b6e0;
    --mint: #9fe0c8;
    --teal: #2fa3c9;
    --blue: #2e6fc0;
    --name-blue: #4a86cf;
    --green: #5bbf8a;
    --red: #e1405a;
    --ink: #6b6b6b;
    --ink-soft: #8c8c8c;
  }
  * { margin: 0; padding: 0; box-sizing: border-box; }
  html, body { width: 1200px; height: 1023px; overflow: hidden; }
  body { background: var(--backdrop); position: relative; font-family: "Patrick Hand", cursive; }

  .card {
    position: absolute; left: 180px; width: 840px; height: 480px;
    background: linear-gradient(160deg, #ffffff 0%, #f4f5f8 100%);
    border-radius: 22px; overflow: hidden;
    box-shadow: 0 10px 28px rgba(60, 50, 40, .25);
  }
  .card--front { top: 22px; }
  .card--back { top: 521px; }
  .card__shapes { position: absolute; inset: 0; }

  /* Front */
  .holder { position: absolute; left: 56px; top: 96px; }
  .holder__name { font-family: "Kalam", cursive; font-size: 38px; color: var(--name-blue); line-height: 1; }
  .holder__title { font-family: "Open Sans", sans-serif; font-size: 16px; color: var(--ink-soft); margin-top: 8px; }

  .offer { position: absolute; left: 56px; top: 222px; font-size: 33px; line-height: 1.15; }
  .offer__visit { color: var(--green); }
  .offer__price { color: var(--teal); }
  .offer__price .accent { color: var(--red); }
  .offer__terms { color: var(--blue); font-size: 28px; }

  .divider { position: absolute; left: 420px; top: 210px; width: 2px; height: 240px; background: var(--blue); }

  .brand { position: absolute; left: 450px; top: 230px; display: flex; align-items: center; gap: 10px; }
  .brand__mark { width: 22px; height: 22px; background: var(--mint); }
  .brand__name { font-family: "Kalam", cursive; font-weight: 700; font-size: 30px; color: var(--teal); }

  .tagline { position: absolute; left: 452px; top: 280px; font-size: 24px; color: var(--ink); line-height: 1.25; }

  .contacts { position: absolute; left: 452px; top: 358px; list-style: none; font-size: 21px; color: var(--green); line-height: 1.3; }
  .contacts li { display: flex; align-items: center; gap: 10px; }
  .contacts svg { width: 18px; height: 18px; flex: none; }

  /* Back */
  .services { position: absolute; list-style: none; font-size: 22px; color: var(--green); line-height: 1.3; }
  .services li { position: relative; padding-left: 30px; }
  .services li::before {
    content: ""; position: absolute; left: 4px; top: 6px; width: 8px; height: 14px;
    border-right: 3px solid var(--blue); border-bottom: 3px solid var(--blue);
    transform: rotate(40deg);
  }
  .services--main { left: 70px; top: 58px; }
  .services--more { left: 480px; top: 222px; }
  .services-title { position: absolute; left: 478px; top: 158px; font-family: "Kalam", cursive; font-weight: 700; font-size: 36px; color: var(--red); line-height: 1.2; }
  .remote-line { position: absolute; left: 60px; top: 420px; font-size: 30px; color: var(--ink); line-height: 1.2; }
</style>
</head>
<body>

<section class="card card--front" aria-label="Card front">
  <svg class="card__shapes" viewBox="0 0 840 480" aria-hidden="true">
    <polygon points="610,0 840,0 840,290 700,420" fill="var(--lavender)" opacity=".55"/>
    <polygon points="700,0 840,0 840,120 735,160" fill="var(--mint)" opacity=".7"/>
  </svg>

  <div class="holder">
    <p class="holder__name">Your Name Here</p>
    <p class="holder__title">Chief Software Engineer</p>
  </div>

  <div class="offer">
    <p class="offer__visit">We come to you</p>
    <p class="offer__price"><span class="accent">Only</span> $49/hr</p>
    <p class="offer__terms">No contract, no monthly fee</p>
  </div>

  <div class="divider"></div>

  <div class="brand">
    <span class="brand__mark"></span>
    <span class="brand__name">GearFix Pro</span>
  </div>

  <p class="tagline">Software engineer on staff<br>remote assistance or visit in your office</p>

  <ul class="contacts">
    <li><svg viewBox="0 0 18 18"><path d="M4 2h3l1 4-2 1a9 9 0 0 0 5 5l1-2 4 1v3a2 2 0 0 1-2 2A14 14 0 0 1 2 4a2 2 0 0 1 2-2z" fill="var(--blue)"/></svg>(005) 555 0142</li>
    <li><svg viewBox="0 0 18 18"><rect x="2" y="2" width="14" height="14" rx="2" fill="none" stroke="var(--blue)" stroke-width="1.6"/></svg>(005) 555 0143</li>
    <li><svg viewBox="0 0 18 18"><rect x="1.5" y="4" width="15" height="10" fill="none" stroke="var(--blue)" stroke-width="1.6"/><path d="M1.5 4l7.5 6 7.5-6" fill="none" stroke="var(--blue)" stroke-width="1.6"/></svg>info@gearfixpro.zone</li>
    <li><svg viewBox="0 0 18 18"><circle cx="9" cy="9" r="7" fill="none" stroke="var(--blue)" stroke-width="1.6"/><path d="M2 9h14M9 2c-3 4-3 10 0 14M9 2c3 4 3 10 0 14" fill="none" stroke="var(--blue)" stroke-width="1.2"/></svg>www.gearfixpro.zone</li>
  </ul>
</section>

<section class="card card--back" aria-label="Card back">
  <svg class="card__shapes" viewBox="0 0 840 480" aria-hidden="true">
    <polygon points="0,40 300,40 140,390 0,390" fill="var(--lavender)" opacity=".75"/>
    <polygon points="180,0 560,0 370,300" fill="var(--mint)" opacity=".7"/>
    <polygon points="440,0 620,0 540,110" fill="var(--lavender)" opacity=".8"/>
  </svg>

  <ul class="services services--main">
    <li>Server setup</li>
    <li>Network troubleshooting</li>
    <li>Printer setup</li>
    <li>Secure backup setup</li>
    <li>Software installation</li>
    <li>Wireless network setup</li>
  </ul>

  <h2 class="services-title">Our Service for you</h2>

  <ul class="services services--more">
    <li>Wired network setup</li>
    <li>Disaster recovery</li>
    <li>Website management</li>
    <li>Any other technology related support</li>
    <li>Email setup</li>
    <li>HIPAA compliance review and setup</li>
  </ul>

  <p class="remote-line">Connect remotely to address your IT issues we go to you</p>
</section>

</body>
</html>
```